Stationary Design for Norvack Digital

We are after a full stationary back business cards, letterheads, compliment slip, invoice template, delivery note and anything else we could use within the stationary pack.

We would also like an email footer creating.

Our company details to be included on all stationary:

Registered Name: Norvack Limited
Company Registration Number: 20483957
Website: www.norvackdigital.example
email: info@norvackdigital.example
Phone: 01632 960 417
Address: 48 Elmstead Lane Loughborough Leicestershire United Kingdom LE14 7QW

Industry/Entity Type

Business

```html
<!DOCTYPE html>
<html lang="en">
<head>
<meta charset="utf-8">
<title>Norvack Digital – Business Card</title>
<link rel="stylesheet" href="https://fonts.googleapis.com/css2?family=Arimo:wght@400;700&display=swap">
<style>
  :root {
    --navy: #12306b;
    --navy-deep: #0b2152;
    --navy-light: #1c4488;
    --ink: #3d3d3d;
    --grey-line: #b9bcc4;
    --paper: #ffffff;
    --backdrop: #e6e7ea;
  }
  * { box-sizing: border-box; margin: 0; padding: 0; }
  html, body { width: 1200px; height: 950px; overflow: hidden; }
  body {
    background: var(--backdrop);
    font-family: "Arimo", Arial, sans-serif;
    position: relative;
  }
  .card {
    position: absolute;
    left: 250px;
    width: 700px;
    height: 400px;
    border-radius: 4px;
    box-shadow: 0 10px 30px rgba(0,0,0,.18);
    overflow: hidden;
  }
  /* Back of card */
  .card--back {
    top: 45px;
    background: linear-gradient(135deg, var(--navy-deep) 0%, var(--navy) 55%, var(--navy-light) 100%);
    color: var(--paper);
    display: flex;
    flex-direction: column;
    align-items: center;
    justify-content: center;
  }
  .card--back .brand-name {
    font-size: 56px;
    font-weight: 700;
    letter-spacing: 1px;
    color: var(--paper);
  }
  .card--back .back-web {
    margin-top: 22px;
    font-size: 18px;
    letter-spacing: 3px;
    color: #d9e1f0;
  }
  /* Front of card */
  .card--front {
    top: 505px;
    background: var(--paper);
  }
  .front-brand {
    position: absolute;
    top: 50px;
    left: 0;
    width: 100%;
    text-align: center;
    font-size: 50px;
    font-weight: 700;
    color: var(--navy);
    letter-spacing: .5px;
    padding-left: 120px;
  }
  .person {
    position: absolute;
    top: 150px;
    right: 375px;
    text-align: right;
  }
  .person__name { font-size: 23px; font-weight: 700; color: var(--navy); }
  .person__role { font-size: 16px; color: var(--navy-light); margin-top: 2px; }
  .contact-list {
    list-style: none;
    margin-top: 14px;
    font-size: 16px;
    color: var(--ink);
    line-height: 26px;
  }
  .contact-list li { display: flex; justify-content: flex-end; align-items: center; gap: 8px; }
  .contact-list svg { width: 15px; height: 15px; flex: none; }
  .divider {
    position: absolute;
    left: 342px;
    top: 205px;
    width: 1px;
    height: 92px;
    background: var(--grey-line);
  }
  .company {
    position: absolute;
    top: 205px;
    left: 362px;
    font-size: 16px;
    color: var(--ink);
    line-height: 21px;
  }
  .company__name { font-weight: 700; }
  .company__reg { margin-top: 12px; }
  .front-band {
    position: absolute;
    left: 0;
    bottom: 0;
    width: 100%;
    height: 58px;
    background: linear-gradient(180deg, var(--navy) 0%, var(--navy-deep) 100%);
    border-top: 6px solid var(--grey-line);
  }
</style>
</head>
<body>

  <section class="card card--back" aria-label="Business card back">
    <div class="brand-name">Norvack Digital</div>
    <div class="back-web">www.norvackdigital.example</div>
  </section>

  <section class="card card--front" aria-label="Business card front">
    <div class="front-brand">Norvack Digital</div>

    <div class="person">
      <div class="person__name">Daniel Hartwell</div>
      <div class="person__role">President</div>
      <ul class="contact-list">
        <li>01632 960 417
          <svg viewBox="0 0 16 16" aria-hidden="true"><circle cx="8" cy="8" r="8" fill="#12306b"/><path d="M5 4.5c.5-.4 1-.4 1.3.1l.7 1.2c.2.4 0 .7-.3 1l-.4.3c.4.9 1.1 1.6 2 2l.3-.4c.3-.3.6-.5 1-.3l1.2.7c.5.3.5.8.1 1.3-.6.7-1.5.9-2.3.5-1.8-.8-3.3-2.3-4.1-4.1-.4-.8-.2-1.7.5-2.3z" fill="#fff"/></svg>
        </li>
        <li>info@norvackdigital.example
          <svg viewBox="0 0 16 16" aria-hidden="true"><circle cx="8" cy="8" r="8" fill="#12306b"/><rect x="4" y="5.2" width="8" height="5.6" rx=".6" fill="#fff"/><path d="M4.2 5.5 8 8.4l3.8-2.9" stroke="#12306b" stroke-width=".9" fill="none"/></svg>
        </li>
        <li>www.norvackdigital.example
          <svg viewBox="0 0 16 16" aria-hidden="true"><circle cx="8" cy="8" r="8" fill="#12306b"/><circle cx="8" cy="8" r="4" stroke="#fff" stroke-width="1" fill="none"/><ellipse cx="8" cy="8" rx="1.7" ry="4" stroke="#fff" stroke-width=".9" fill="none"/><path d="M4 8h8" stroke="#fff" stroke-width=".9"/></svg>
        </li>
      </ul>
    </div>

    <div class="divider"></div>

    <address class="company" style="font-style:normal">
      <div class="company__name">Norvack Limited</div>
      <div>48 Elmstead Lane Loughborough</div>
      <div>Leicestershire</div>
      <div>United Kingdom LE14 7QW</div>
      <div class="company__reg">Reg. No: 20483957</div>
    </address>

    <div class="front-band"></div>
  </section>

</body>
</html>
```